Financial Services Company Needs New UI/UX

Hello!

We would like to see some UI/UX ideas for our software platform. I've attached a screen capture of our current "dashboard" (or main home page, essentially). We're looking for a very simple, clean, sleek design as there are many different pages throughout the system that will all need to coordinate. You can also view our website to see the colors and general "look" we have on there. It would be ideal for the portal to coordinate with the website since that is how they access the login page. Please submit your best ideas for the dashboard and we will reach out to our favorite designer to move forward with the rest of the pages. You can find our color hex codes on our website on the "Media" page. Should you need any other supporting logos or files please send us a message and we will try to accommodate.

Thanks!

Website: www.lendmarkbuilt.example

Target Market(s)

Our clients are contractors in the construction industry and our software helps them manage material purchases for their jobs.

Industry/Entity Type

Financial Service

Font styles to use
Sans Serif

Requirements
Must have
• The same content and language as the current dashboard but an updated look.
Should not have
• Too much distraction or busy patterns, we're looking for clean and simple and user friendly. Likely a solid or subtly textured background would be best.

```html
<!DOCTYPE html>
<html lang="en">
<head>
<meta charset="utf-8">
<title>Quarrybend Dashboard</title>
<link rel="stylesheet" href="https://fonts.googleapis.com/css2?family=Roboto:wght@300;400;500&display=swap">
<style>
  :root {
    --bg: #414852;
    --panel: #666c77;
    --inset: #858c96;
    --row-dark: #4b525c;
    --accent: #4a88e4;
    --text: #ffffff;
    --text-soft: #e9ecf0;
    --text-faint: #535b66;
    --avatar: #5b6f93;
  }
  * { box-sizing: border-box; margin: 0; padding: 0; }
  html, body { width: 1200px; height: 900px; overflow: hidden; }
  body {
    background: var(--bg);
    font-family: "Roboto", Arial, sans-serif;
    font-weight: 300;
    color: var(--text);
    position: relative;
  }
  .abs { position: absolute; }

  /* Header */
  .brand { left: 20px; top: 34px; display: flex; align-items: center; gap: 8px; }
  .brand-dot { width: 38px; height: 38px; border-radius: 50%; background: var(--text); }
  .brand-name { font-size: 18px; font-weight: 400; color: var(--text); }
  .divider { top: 16px; width: 2px; height: 76px; background: var(--text-soft); }
  .page-title { left: 230px; top: 36px; font-size: 30px; color: var(--accent); font-weight: 300; }
  .avatar { left: 428px; top: 28px; width: 54px; height: 54px; border-radius: 50%; background: var(--avatar); }
  .greeting { left: 498px; top: 32px; font-size: 13px; line-height: 24px; color: var(--text-faint); font-weight: 400; }
  .menu-grid { left: 1147px; top: 39px; }

  /* Summary cards */
  .card { background: var(--panel); top: 134px; width: 376px; height: 333px; }
  .card-title { position: absolute; left: 0; right: 0; top: 42px; text-align: center; font-size: 24px; font-weight: 300; }
  .amount { position: absolute; left: 0; right: 0; top: 64px; text-align: center; font-size: 48px; line-height: 60px; font-weight: 300; }
  .amount .cur { font-size: 26px; vertical-align: 20px; margin-right: 2px; }
  .amount .cents { font-size: 24px; }
  .inset { position: absolute; left: 22px; width: 328px; background: var(--inset); text-align: center; color: var(--text-soft); }
  .inset-label { font-size: 13px; font-weight: 300; color: #f2f4f6; }
  .inset-value { font-size: 17px; font-weight: 300; margin-top: 3px; }
  .btn { position: absolute; top: 248px; height: 40px; background: var(--accent); color: var(--text); font-size: 18px; font-weight: 300; display: flex; align-items: center; justify-content: center; }
  .due-line { font-size: 13px; font-weight: 300; line-height: 22px; }
  .due-line b { font-size: 17px; font-weight: 300; margin-left: 3px; }

  /* Lower panels */
  .panel { background: var(--panel); top: 488px; height: 392px; }
  .panel-title { position: absolute; left: 26px; top: 32px; font-size: 24px; font-weight: 300; }
  .th { position: absolute; font-size: 17px; font-weight: 500; }
  .row { position: absolute; left: 22px; }
  .row.dark { background: var(--row-dark); }
  .cell { position: absolute; font-size: 15px; font-weight: 300; line-height: 24px; }
  .help { position: absolute; left: 10px; width: 21px; height: 21px; border-radius: 50%; background: var(--accent); color: var(--row-dark); font-size: 14px; font-weight: 500; text-align: center; line-height: 21px; }
  .job-cell { position: absolute; top: 7px; font-size: 14px; font-weight: 300; }
</style>
</head>
<body>

<header>
  <div class="abs brand"><span class="brand-dot"></span><span class="brand-name">Quarrybend</span></div>
  <span class="abs divider" style="left:205px"></span>
  <h1 class="abs page-title">Dashboard</h1>
  <span class="abs divider" style="left:403px"></span>
  <div class="abs avatar" role="img" aria-label="User profile picture"></div>
  <div class="abs greeting">Hello User,<br>6/30/2016&nbsp; 03:08:21 AM</div>
  <svg class="abs menu-grid" width="32" height="32" viewBox="0 0 32 32" aria-label="Menu">
    <rect x="0" y="0" width="14" height="14" fill="#4a88e4"/>
    <rect x="17" y="0" width="14" height="14" fill="#4a88e4"/>
    <rect x="0" y="17" width="14" height="14" fill="#4a88e4"/>
    <rect x="17" y="17" width="14" height="14" fill="#4a88e4"/>
  </svg>
</header>

<main>
  <section class="abs card" style="left:20px">
    <h2 class="card-title">Available Master Credit</h2>
    <div class="amount"><span class="cur">$</span>129,500<span class="cents">.00</span></div>
    <div class="inset" style="top:176px;height:54px;padding-top:8px">
      <div class="inset-label">Master Credit Limit</div>
      <div class="inset-value">$250,000.00</div>
    </div>
    <div class="btn" style="left:23px;width:327px">Setup New Job</div>
  </section>

  <section class="abs card" style="left:416px">
    <h2 class="card-title">Last Payment</h2>
    <div class="amount"><span class="cur">$</span>500<span class="cents">.00</span></div>
    <div class="inset" style="left:19px;top:176px;height:54px;padding-top:8px">
      <div class="inset-label">Last Payment Date</div>
      <div class="inset-value">6/28/2016</div>
    </div>
    <div class="btn" style="left:19px;width:155px">View Payments</div>
    <div class="btn" style="left:194px;width:152px">View Billings</div>
  </section>

  <section class="abs card" style="left:804px">
    <h2 class="card-title">Next Payment</h2>
    <div class="amount"><span class="cur">$</span>158<span class="cents">.95</span></div>
    <div class="inset" style="top:147px;height:83px;padding-top:9px">
      <div class="due-line">Due Date <b>7/11/2016</b></div>
      <div class="due-line">Current Principal <b>$9,968.46</b></div>
      <div class="due-line">Minimum Interest/Fee <b>$158.95</b></div>
    </div>
    <div class="btn" style="left:23px;width:327px">Make Payment</div>
  </section>

  <section class="abs panel" style="left:20px;width:570px">
    <h2 class="panel-title">Task Summary</h2>
    <div class="th" style="left:64px;top:88px">Task</div>
    <div class="th" style="left:240px;top:88px">Status</div>
    <div class="th" style="left:433px;top:88px">Received</div>

    <div class="row dark" style="top:117px;width:523px;height:59px">
      <span class="help" style="top:8px">?</span>
      <span class="cell" style="left:42px;top:7px">Supplier Invoice</span>
      <span class="cell" style="left:218px;top:7px">Confirmation by<br>Account Manager</span>
      <span class="cell" style="left:411px;top:7px">5/10/2016</span>
    </div>
    <div class="row" style="top:176px;width:523px;height:60px">
      <span class="help" style="top:8px">?</span>
      <span class="cell" style="left:42px;top:7px">Supplier Invoice</span>
      <span class="cell" style="left:218px;top:7px">Confirmation by<br>Account Manager</span>
      <span class="cell" style="left:411px;top:7px">5/09/2016</span>
    </div>
    <div class="row dark" style="top:236px;width:523px;height:60px">
      <span class="help" style="top:8px">?</span>
      <span class="cell" style="left:42px;top:7px">Supplier Invoice</span>
      <span class="cell" style="left:218px;top:7px">Confirmation by<br>Account Manager</span>
      <span class="cell" style="left:411px;top:7px">5/07/2016</span>
    </div>
    <div class="row" style="top:296px;width:523px;height:60px">
      <span class="help" style="top:8px">?</span>
      <span class="cell" style="left:42px;top:8px">Supplier Invoice</span>
      <span class="cell" style="left:214px;top:8px">Confirmation by<br>Account Manager</span>
      <span class="cell" style="left:411px;top:8px">5/04/2016</span>
    </div>
  </section>

  <section class="abs panel" style="left:610px;width:570px">
    <h2 class="panel-title">Active Jobs</h2>
    <div class="th" style="left:30px;top:93px">Job #</div>
    <div class="th" style="left:116px;top:93px">Job Name</div>
    <div class="th" style="left:222px;top:93px">Status</div>
    <div class="th" style="left:303px;top:93px">Credit Limit</div>
    <div class="th" style="left:431px;top:93px">Avail. Credits</div>

    <div class="row dark" style="top:130px;width:523px;height:32px">
      <span class="job-cell" style="left:9px">PC101-001</span>
      <span class="job-cell" style="left:92px">Job #001</span>
      <span class="job-cell" style="left:198px">Active</span>
      <span class="job-cell" style="left:281px">$50,100,00</span>
      <span class="job-cell" style="left:408px">$35,100,00</span>
    </div>
    <div class="row" style="top:166px;width:523px;height:32px">
      <span class="job-cell" style="left:9px">PC101-002</span>
      <span class="job-cell" style="left:92px">Job #002</span>
      <span class="job-cell" style="left:198px">Active</span>
      <span class="job-cell" style="left:281px">$40.000,00</span>
      <span class="job-cell" style="left:408px">$2.000,00</span>
    </div>
    <div class="row dark" style="top:202px;width:523px;height:32px">
      <span class="job-cell" style="left:9px">PC101-003</span>
      <span class="job-cell" style="left:92px">Job #003</span>
      <span class="job-cell" style="left:198px">Active</span>
      <span class="job-cell" style="left:281px">$22,000,00</span>
      <span class="job-cell" style="left:408px">$0,00</span>
    </div>
    <div class="row" style="top:238px;width:523px;height:32px">
      <span class="job-cell" style="left:9px">PC101-004</span>
      <span class="job-cell" style="left:92px">Job #004</span>
      <span class="job-cell" style="left:198px">Active</span>
      <span class="job-cell" style="left:281px">$10,400,00</span>
      <span class="job-cell" style="left:408px">$10,400,00</span>
    </div>
    <div class="row dark" style="top:275px;width:523px;height:32px"></div>
  </section>
</main>

</body>
</html>
```